Innovative Health and Beauty business needs a clean Brand Image -

We need a logo designed and packaging for a new company. We are developing safe, easy to use, and reliable products to help people in health and beauty industry. We would like creative, clean, and elegant branding to elevate brand integrity and customer service focus.

```html
<!DOCTYPE html>
<html lang="en">
<head>
<meta charset="utf-8">
<title>Lumiva – Inflatable Shampoo Bowl Packaging</title>
<link rel="stylesheet" href="https://fonts.googleapis.com/css2?family=Fredoka:wght@500;600;700&family=Cormorant+Garamond:wght@500&family=Montserrat:wght@500&display=swap">
<style>
  :root {
    --bg: #e4e4e4;
    --white: #f4f4f2;
    --green: #9fcd85;
    --green-deep: #6bb04e;
    --teal: #1f4a52;
    --teal-soft: #2f565d;
    --ink: #2a4d55;
    --photo-warm: #d9d2cc;
    --photo-cool: #ecebe8;
  }
  * { box-sizing: border-box; margin: 0; padding: 0; }
  html, body { width: 1200px; height: 720px; overflow: hidden; }
  body { background: var(--bg); font-family: "Fredoka", sans-serif; position: relative; }

  .panel { position: absolute; overflow: hidden; }

  /* Lid */
  .lid { left: 60px; top: 60px; width: 700px; height: 380px; background: var(--white); }
  .lid .brand { position: absolute; left: 40px; top: 34px; font-family: "Cormorant Garamond", serif; font-weight: 500; font-size: 40px; letter-spacing: 8px; color: var(--ink); }
  .lid .title { position: absolute; left: 40px; top: 110px; font-weight: 700; font-size: 44px; line-height: 1.05; color: var(--green-deep); }
  .lid .wave { position: absolute; left: 0; top: 0; width: 700px; height: 380px; }
  .lid .product-photo { position: absolute; left: 400px; top: 170px; width: 250px; height: 180px; border-radius: 46% 46% 40% 40%; background: radial-gradient(circle at 50% 45%, #fbf8ef, #e6e0d2); }

  /* Front side */
  .front { left: 60px; top: 460px; width: 700px; height: 200px; background: var(--white); }
  .features { position: absolute; left: 24px; top: 28px; display: flex; gap: 14px; z-index: 2; }
  .feature { width: 86px; text-align: center; }
  .feature .icon { width: 66px; height: 66px; border-radius: 50%; background: var(--green); margin: 0 auto 10px; display: flex; align-items: center; justify-content: center; }
  .feature .label { font-weight: 600; font-size: 12px; line-height: 1.15; color: var(--ink); }
  .front .scene-photo { position: absolute; right: 0; top: 0; width: 250px; height: 200px; background: linear-gradient(100deg, var(--photo-cool), var(--photo-warm) 70%, #3a3f55); }
  .front .curve { position: absolute; left: 420px; top: 0; width: 100px; height: 200px; }

  /* End flap */
  .end { left: 790px; top: 60px; width: 350px; height: 380px; background: var(--green); padding: 34px 30px; color: var(--white); }
  .end .brand { font-family: "Cormorant Garamond", serif; font-weight: 500; font-size: 30px; letter-spacing: 6px; color: var(--white); }
  .end .title { margin-top: 22px; font-weight: 700; font-size: 34px; line-height: 1.05; }
  .end .copy { margin-top: 18px; font-family: "Montserrat", sans-serif; font-weight: 500; font-size: 11.5px; line-height: 1.55; }
  .end .copy p + p { margin-top: 8px; }

  /* Interior print */
  .interior { left: 790px; top: 460px; width: 350px; height: 200px; background: linear-gradient(160deg, var(--teal-soft), var(--teal)); }
</style>
</head>
<body>

<section class="panel lid">
  <svg class="wave" viewBox="0 0 700 380" aria-hidden="true">
    <path d="M230 380 C 290 250, 420 170, 560 160 C 630 155, 680 170, 700 185 L700 380 Z" fill="var(--green)"/>
  </svg>
  <div class="brand">LUMIVA</div>
  <h1 class="title">Inflatable<br>Shampoo Bowl</h1>
  <div class="product-photo" role="img" aria-label="Photo of the white inflatable shampoo bowl"></div>
</section>

<section class="panel front">
  <div class="features">
    <div class="feature">
      <div class="icon">
        <svg width="38" height="38" viewBox="0 0 40 40" aria-hidden="true" fill="#fff">
          <path d="M20 4 C 24 11, 27 14, 27 18 a7 7 0 0 1 -14 0 C13 14, 16 11, 20 4Z"/>
          <path d="M11 20 C 14 25, 16 27, 16 30 a5 5 0 0 1 -10 0 C6 27, 8 25, 11 20Z"/>
          <path d="M29 20 C 32 25, 34 27, 34 30 a5 5 0 0 1 -10 0 C24 27, 26 25, 29 20Z"/>
        </svg>
      </div>
      <div class="label">Thick PVC Material</div>
    </div>
    <div class="feature">
      <div class="icon">
        <svg width="38" height="38" viewBox="0 0 40 40" aria-hidden="true" stroke="#fff" stroke-width="2.5" fill="none" stroke-linecap="round">
          <line x1="6" y1="17" x2="34" y2="17"/><line x1="6" y1="23" x2="34" y2="23"/>
          <path d="M20 4 V13 M16 9 L20 13 L24 9"/><path d="M20 36 V27 M16 31 L20 27 L24 31"/>
        </svg>
      </div>
      <div class="label">Double-Layered Air Valve</div>
    </div>
    <div class="feature">
      <div class="icon">
        <svg width="38" height="38" viewBox="0 0 40 40" aria-hidden="true" fill="#fff">
          <rect x="8" y="5" width="24" height="5" rx="1"/>
          <path d="M15 10 H25 L22 22 H18 Z"/>
          <path d="M20 26 C 22 30, 24 31, 24 33 a4 4 0 0 1 -8 0 C16 31, 18 30, 20 26Z"/>
        </svg>
      </div>
      <div class="label">Drain Hole With Plug</div>
    </div>
    <div class="feature">
      <div class="icon">
        <svg width="38" height="38" viewBox="0 0 40 40" aria-hidden="true" stroke="#fff" stroke-width="2.5" fill="none" stroke-linejoin="round">
          <path d="M7 8 Q20 5 33 8 Q36 20 33 32 Q20 35 7 32 Q4 20 7 8Z"/>
          <path d="M13 16 V26 H22"/>
        </svg>
      </div>
      <div class="label">Large Inflatable Panel</div>
    </div>
  </div>
  <div class="scene-photo" role="img" aria-label="Photo of a person lying back with their head resting in the inflatable shampoo bowl"></div>
  <svg class="curve" viewBox="0 0 100 200" aria-hidden="true">
    <path d="M0 0 H50 C 30 60, 45 130, 100 200 H0 Z" fill="var(--white)"/>
  </svg>
</section>

<section class="panel end">
  <div class="brand">LUMIVA</div>
  <h2 class="title">Inflatable<br>Shampoo Bowl</h2>
  <div class="copy">
    <p>Portable shampoo basin makes it easy to wash a loved one's hair while they rest in bed.</p>
    <p>Designed for comfort with a built-in neck rest.</p>
    <p>Extra deep inflatable basin built from durable heavy duty vinyl, easy to clean.</p>
  </div>
</section>

<section class="panel interior" aria-label="Box interior print"></section>

</body>
</html>
```